Skin Care Package Design

Hello,

I have a unique situation at hand. I already posted a project for this and we chose a winner but we ended up having trademark concerns so we need to modify the designs on the package.

We do not blame the designer in any way and we think that they did an incredible job. We have also chosen him as the winner and paid him so we have full right to share this and have 100% ownership of the design.

Our biggest competitor is Lumo Brisk Dot. We need to be careful not to have a design that is too close to theirs. I think the color red is fine in general, but we need to stay away from any shapes/designs that would be considered similar. They have a partial circle design on the corner and ours is to similar in our opinion - our mistake.

Our name is no longer Velden Face Co. It is now TOLVEN or Tolven.

We need:
1. Velden Face Co removed and "TOLVEN" or "Tolven" put in it's place. You do NOT have to leave the rectangle border. We do not have a design file or the logo yet. We like modern fonts.
2. Please remove the circular designs in the corners. It too closely resembles our competitors package. A square or some other unique concept would work. Feel free to use your imagination. We loved our current design because it's clean and simple but looks good.
3. Please don't mess with the text. We like it and the layout. Our focus is on the color/s and unique design that is going to replace the circle in the corners.
4. Please change "144" in the bottom right to "36".
5. The color red is still fine but we would be curious to see other colors like the green or blue that Dunmel has or maybe a taupe. Use your imagination. We really want colors that pop and grab your attention. Feel free to use more than one color.

I have uploaded two images.
1. Lumo - Is our competitor's package.
2. Velden Face Co is our previous/current package design.

Package deminsions: 5”x3.4”x0.47”

Thanks! Good luck!

Target Market(s)

Male & female. We don't want the package design to be too masculine or too feminine.

Industry/Entity Type

Skin care, health & cosmetics.

Font styles to use
Sans Serif

Requirements
Must have
• You can search acne patch brands on Shopnest and see our competitors. We want ours to look better than Lumo Brisk Dot. They are the top seller. They have a simple and clean design but the red really grabs your eye. There are a ton of brands on the Shopnest page so it's important that the package looks good and the color/s catch your eye.

```html
<!DOCTYPE html>
<html lang="en">
<head>
<meta charset="UTF-8">
<title>Tolven – The Acne Patch</title>
<link rel="stylesheet" href="https://fonts.googleapis.com/css2?family=Montserrat:wght@300;400;500;600;700;800&display=swap">
<style>
  :root {
    --backdrop: #e6e0cb;
    --olive: #7f6d22;
    --olive-text: #84742c;
    --apricot: #e8a15a;
    --card-top: #fcf1eb;
    --card-bottom: #f7ebe1;
    --hole: #f8f6ef;
    --patch-blue: #bfdce6;
    --patch-edge: #8fc3d6;
  }
  * { margin: 0; padding: 0; box-sizing: border-box; }
  html, body {
    width: 1200px; height: 1200px; overflow: hidden;
    background: var(--backdrop);
    font-family: "Montserrat", sans-serif;
  }
  .canvas { position: relative; width: 1200px; height: 1200px; }

  .hang-tab {
    position: absolute; left: 347px; top: 175px; width: 465px; height: 88px;
    background: var(--olive);
  }
  .hang-tab svg { position: absolute; left: 198px; top: 16px; }

  .package-front {
    position: absolute; left: 341px; top: 262px; width: 478px; height: 723px;
    background: linear-gradient(160deg, var(--card-top), var(--card-bottom));
    overflow: hidden;
  }
  .package-front > * { position: absolute; }

  .brand-name {
    left: 42px; top: 112px;
    font-weight: 500; font-size: 38px; letter-spacing: 3px; line-height: 1;
    color: var(--olive);
  }

  .swirl-art {
    left: 319px; top: -7px; width: 136px; height: 192px;
    background: radial-gradient(ellipse at center, rgba(127,109,34,0.10), rgba(127,109,34,0.02) 70%);
  }
  .flower-art {
    left: 0; top: 609px; width: 110px; height: 114px;
    background: radial-gradient(ellipse at 40% 40%, rgba(232,161,90,0.18), rgba(232,161,90,0.04) 70%);
  }
  .patch-art {
    left: 347px; top: 267px; width: 117px; height: 115px;
    border-radius: 50%;
    background: radial-gradient(circle at 60% 55%, var(--patch-blue), var(--patch-edge));
  }

  .product-title { left: 44px; top: 232px; line-height: 65px; font-size: 69px; }
  .product-title span { display: block; }
  .title-the { color: var(--apricot); font-weight: 400; }
  .title-acne { color: var(--olive); font-weight: 800; }
  .title-patch { color: var(--olive); font-weight: 400; }

  .tagline-rule { left: 46px; top: 449px; width: 62px; height: 5px; background: var(--apricot); }
  .tagline {
    left: 131px; top: 442px;
    font-size: 14.2px; font-weight: 700; line-height: 18px; color: var(--apricot); white-space: nowrap;
  }
  .tagline-arrow { left: 320px; top: 400px; }

  .usage {
    left: 44px; top: 474px;
    font-size: 33px; font-weight: 300; line-height: 34px; color: var(--olive-text);
  }
  .description {
    left: 45px; top: 562px;
    font-size: 14.5px; font-weight: 400; line-height: 16.8px; color: var(--olive-text); white-space: nowrap;
  }
  .count-badge { left: 332px; top: 557px; }
</style>
</head>
<body>
<div class="canvas">
  <div class="hang-tab">
    <svg width="69" height="48" viewBox="0 0 69 48">
      <path fill="var(--hole)" d="M20 47 H52 a15 15 0 0 0 0-30 h-4 a14 14 0 0 0-27 0 h-3 a15 15 0 0 0 0 30 z"/>
    </svg>
  </div>

  <div class="package-front">
    <div class="swirl-art" role="img" aria-label="Decorative olive line spiral"></div>

    <div class="brand-name">TOLVEN</div>

    <div class="product-title">
      <span class="title-the">THE</span>
      <span class="title-acne">ACNE</span>
      <span class="title-patch">PATCH</span>
    </div>

    <div class="patch-art" role="img" aria-label="Clear blue hydrocolloid patch peeling up"></div>

    <div class="tagline-rule"></div>
    <div class="tagline">YOUR BLEMISH WIZARD</div>
    <svg class="tagline-arrow" width="80" height="60" viewBox="0 0 80 60">
      <path d="M7 52 C40 52 55 40 60 18" fill="none" stroke="var(--apricot)" stroke-width="4" stroke-linecap="round"/>
      <path d="M53 20 L63 8 L68 23 Z" fill="var(--apricot)"/>
    </svg>

    <div class="usage">Ideal for<br>surface spots</div>
    <p class="description">Gently absorbs gunk in 6 - 8 hours<br>&amp; approves the look of pimples<br>overnight.</p>

    <svg class="count-badge" width="150" height="150" viewBox="0 0 150 150">
      <defs>
        <path id="badge-top" d="M19 90 A58 58 0 1 1 131 90"/>
        <path id="badge-bottom" d="M24.6 114.4 A64 64 0 0 0 125.4 114.4"/>
      </defs>
      <g fill="var(--olive)" font-family="Montserrat, sans-serif">
        <text font-size="11.5" font-weight="500" letter-spacing="3">
          <textPath href="#badge-top" startOffset="50%" text-anchor="middle">8 MM &amp; 12 MM SIZES</textPath>
        </text>
        <text font-size="11.5" font-weight="500" letter-spacing="3">
          <textPath href="#badge-bottom" startOffset="50%" text-anchor="middle">NON - DRYING</textPath>
        </text>
        <text x="20.6" y="102" font-size="7" text-anchor="middle">★</text>
        <text x="129.4" y="102" font-size="7" text-anchor="middle">★</text>
        <text x="75" y="88" font-size="58" font-weight="800" text-anchor="middle" letter-spacing="-1">36</text>
        <text x="75" y="101" font-size="10" font-weight="500" text-anchor="middle">HYDROCOLLOID</text>
        <text x="75" y="112" font-size="10" font-weight="500" text-anchor="middle">PATCHES</text>
      </g>
    </svg>

    <div class="flower-art" role="img" aria-label="Outlined apricot flower petals"></div>
  </div>
</div>
</body>
</html>
```